Business Card Design Project

I want a cleaner business card and envelope then what we have now, its too crowded.
Updates

I update with logo, this can be changed anyway you feel it looks best. I also have put gaurantee on there and extended time, this is my first time doing this. Also gave an example of current card

Target Market(s)

a wide array of customers from lattice 700 to small companies and cleints

Industry/Entity Type

Business

Requirements
Must have
• Need to have address, telephone number email
Nice to have
• a sharp professional card that stands out but is still very clean.
Should not have
• Not crazy looking

```html
<!DOCTYPE html>
<html lang="en">
<head>
<meta charset="utf-8">
<title>Marlow Insurance Group – Business Card</title>
<link rel="stylesheet" href="https://fonts.googleapis.com/css2?family=Montserrat:wght@500&family=Sorts+Mill+Goudy&family=Open+Sans:wght@600&display=swap">
<style>
  :root {
    --page: #ffffff;
    --front-top: #a8abae;
    --front-bottom: #ececec;
    --mark-dark: #1f1f1f;
    --mark-mid: #4a4a4a;
    --ink-front: #2a2a2a;
    --back-base: #2e2e2e;
    --back-glow: #454545;
    --ink-back: #f2f2f2;
    --ink-muted: #b9b9b9;
    --shadow: rgba(0, 0, 0, 0.45);
  }
  * { box-sizing: border-box; margin: 0; padding: 0; }
  html, body { width: 1200px; height: 900px; overflow: hidden; background: var(--page); }
  .canvas { position: relative; width: 1200px; height: 900px; }

  .card { position: absolute; width: 769px; height: 439px; box-shadow: 3px 4px 5px var(--shadow); }

  .card-front {
    left: 37px; top: 44px; z-index: 2;
    background: linear-gradient(180deg, var(--front-top) 0%, #c9cacc 50%, var(--front-bottom) 100%);
  }
  .brand-square {
    position: absolute; left: 338px; top: 134px; width: 96px; height: 98px;
    background: linear-gradient(180deg, var(--mark-dark), var(--mark-mid));
  }
  .brand-name {
    position: absolute; left: 0; right: 0; top: 244px; text-align: center;
    font-family: "Montserrat", sans-serif; font-weight: 500; color: var(--ink-front);
  }
  .brand-name .primary { display: block; font-size: 34px; letter-spacing: 4px; line-height: 40px; }
  .brand-name .secondary { display: block; font-size: 17px; letter-spacing: 3.4px; line-height: 24px; }

  .card-back {
    left: 389px; top: 431px; z-index: 1;
    background: radial-gradient(ellipse 70% 60% at 55% 40%, var(--back-glow) 0%, var(--back-base) 100%);
  }
  .holder {
    position: absolute; left: 0; width: 492px; top: 162px; text-align: center;
  }
  .holder-name {
    font-family: "Sorts Mill Goudy", serif; font-size: 42px; font-weight: 400;
    color: var(--ink-back); line-height: 52px;
  }
  .holder-title {
    font-family: "Open Sans", sans-serif; font-weight: 600; font-size: 14px;
    letter-spacing: 1px; color: var(--ink-muted); line-height: 20px;
  }
  .holder-address {
    margin-top: 12px; font-family: "Sorts Mill Goudy", serif; font-size: 12.5px;
    color: var(--ink-back); line-height: 16px;
  }
  .divider {
    position: absolute; left: 481px; top: 125px; width: 1.5px; height: 190px;
    background: linear-gradient(180deg, transparent, #9a9a9a 50%, transparent);
  }
  .contact-list {
    position: absolute; left: 519px; top: 178px; list-style: none;
    font-family: "Sorts Mill Goudy", serif; font-size: 14px; color: var(--ink-back);
  }
  .contact-list li { display: flex; align-items: center; height: 21.5px; }
  .contact-list svg { width: 17px; height: 17px; margin-right: 7px; flex: none; }
</style>
</head>
<body>
<main class="canvas">
  <section class="card card-front" aria-label="Card front">
    <div class="brand-square"></div>
    <h1 class="brand-name">
      <span class="primary">MARLOW</span>
      <span class="secondary">INSURANCE GROUP</span>
    </h1>
  </section>

  <section class="card card-back" aria-label="Card back">
    <div class="holder">
      <h2 class="holder-name">Renata Holm - Vesey</h2>
      <p class="holder-title">OPERATION MANAGER</p>
      <p class="holder-address">18240 Alder Park Ave. Marlow Heights, MI 48000 www.marlowagency.com</p>
    </div>
    <div class="divider"></div>
    <ul class="contact-list">
      <li>
        <svg viewBox="0 0 16 16" aria-hidden="true"><rect width="16" height="16" fill="#e6e6e6"/><path d="M4.5 3.5l2 .2.8 2.3-1.2 1a6 6 0 0 0 3 3l1-1.2 2.3.8.1 2a1 1 0 0 1-1 1A8.5 8.5 0 0 1 3.5 4.5a1 1 0 0 1 1-1z" fill="#2e2e2e"/></svg>
        555-014-2700 ext 232
      </li>
      <li>
        <svg viewBox="0 0 16 16" aria-hidden="true"><rect width="16" height="16" fill="#e6e6e6"/><rect x="5" y="2.5" width="6" height="11" rx="1" fill="none" stroke="#2e2e2e" stroke-width="1.3"/><circle cx="8" cy="11.5" r=".7" fill="#2e2e2e"/></svg>
        555-014-0138 (direct)
      </li>
      <li>
        <svg viewBox="0 0 16 16" aria-hidden="true"><rect width="16" height="16" fill="#e6e6e6"/><rect x="4.5" y="3" width="7" height="3.5" fill="#2e2e2e"/><rect x="3" y="7" width="10" height="5" fill="#2e2e2e"/><rect x="5" y="10" width="6" height="3" fill="#e6e6e6"/></svg>
        555-014-2703
      </li>
      <li>
        <svg viewBox="0 0 16 16" aria-hidden="true"><rect width="16" height="16" fill="#e6e6e6"/><rect x="2.5" y="4" width="11" height="8" fill="#2e2e2e"/><path d="M2.5 4l5.5 4.5L13.5 4" fill="none" stroke="#e6e6e6" stroke-width="1"/></svg>
        rholm-vesey@marlowagency.com
      </li>
    </ul>
  </section>
</main>
</body>
</html>
```